Apartment Ratings Card

I need a new, trendy design for an Apartment Rating card that we hand out to residents at our apartments asking them to give us a review. Attached is what we currently hand out, but I need the new one to have a general picture or graphic that is fun and modern.
I need a new headline, use your imagination, but here are a few I like:
Be a Not-So-Secret Admirer
Love Us/Rate Us/Share Us
Copy:
Thank you for your recent visit to our office. We want to provide you with +1 Customer Service. Would you consider posting a review of us online? in addition to providing feedback, online reviews can help other customers learn about who we are and reviews are a great way to give a referral to your family and friends.
Please include the following logos:
Flatscorehub.net
Chatterloop
Zendro Business
Vantly
Be creative and add anything you have seen to help us stand out.
Target Market(s)
Resident who live at our apartment communities and potential renters.
Industry/Entity Type
Real Estate
Colors
Designer to choose colors to be used in the design.
Look and feel

```html
<!DOCTYPE html>
<html lang="en">
<head>
<meta charset="utf-8">
<title>Have your say! – Review Card</title>
<link rel="stylesheet" href="https://fonts.googleapis.com/css2?family=Lobster&family=Raleway:wght@300;400&family=Mulish:wght@400;600&family=Open+Sans:wght@600&display=swap">
<style>
  :root {
    --sky: #0aaeea;
    --sky-soft: #8fd8f5;
    --paper: #f4f5f6;
    --ink: #3b4858;
    --title-blue: #1a9fd8;
    --deep-blue: #15609f;
    --white: #ffffff;
    --tile-1: #1b6aa6;
    --tile-2: #2a86c8;
    --tile-3: #4aa3d9;
    --tile-4: #0e4f86;
  }
  * { margin: 0; padding: 0; box-sizing: border-box; }
  html, body { width: 816px; height: 1200px; overflow: hidden; background: var(--paper); }
  .card { position: relative; width: 816px; height: 1200px; overflow: hidden; background: var(--paper); }
  .card-waves { position: absolute; inset: 0; }

  .headline {
    position: absolute; top: 52px; left: 0; width: 816px; text-align: center;
    font-family: "Lobster", cursive; font-weight: 400; font-size: 66px; color: var(--white);
    line-height: 1;
  }
  .tagline {
    position: absolute; top: 140px; left: 0; width: 816px; text-align: center;
    font-family: "Raleway", sans-serif; font-weight: 300; font-size: 35px; letter-spacing: 3px;
    color: var(--white);
  }
  .tagline .dot { font-size: 22px; vertical-align: 5px; margin: 0 8px; }

  .intro, .pitch {
    position: absolute; left: 102px; width: 612px;
    font-family: "Mulish", sans-serif; font-size: 22px; line-height: 28px; color: var(--ink);
  }
  .intro { top: 284px; }
  .question {
    position: absolute; top: 360px; left: 102px; width: 640px;
    font-family: "Lobster", cursive; font-size: 28px; color: var(--title-blue);
  }
  .pitch { top: 420px; }

  .illustration {
    position: absolute; left: 118px; top: 553px; width: 557px; height: 190px;
    border-radius: 6px;
    background: linear-gradient(90deg, #d81e5b 0%, #a9c23a 30%, #f5b81a 55%, #27b3cc 78%, #1b5e9c 100%);
    opacity: .85;
  }
  .illustration::after {
    content: ""; position: absolute; left: 0; right: 0; bottom: 0; height: 30px;
    background: #e2dccf; border-radius: 0 0 6px 6px;
  }

  .cta {
    position: absolute; top: 752px; left: 0; width: 816px; text-align: center;
    font-family: "Open Sans", sans-serif; font-weight: 600; font-size: 47px; color: var(--title-blue);
  }
  .cta .accent { color: var(--deep-blue); }

  .review-sites {
    position: absolute; top: 840px; left: 110px; width: 600px;
    display: flex; justify-content: space-between; align-items: center; list-style: none;
  }
  .review-site {
    display: flex; align-items: center; gap: 8px;
    font-family: "Mulish", sans-serif; font-weight: 600; font-size: 19px; color: var(--deep-blue);
  }
  .review-site .swatch { width: 18px; height: 18px; }

  .brand {
    position: absolute; top: 1000px; left: 0; width: 816px; text-align: center;
    font-family: "Raleway", sans-serif; font-weight: 300; color: var(--white);
  }
  .brand-name { font-size: 58px; letter-spacing: 22px; line-height: 1; padding-left: 22px; }
  .brand-sub { font-size: 24px; letter-spacing: 2px; margin-top: 10px; }
  .brand-kind { font-size: 11px; letter-spacing: 4px; margin-top: 2px; padding-left: 230px; }
  .website {
    position: absolute; top: 1122px; left: 0; width: 816px; text-align: center;
    font-family: "Mulish", sans-serif; font-size: 19px; color: var(--white); padding-left: 30px;
  }
</style>
</head>
<body>
<main class="card">
  <svg class="card-waves" width="816" height="1200" viewBox="0 0 816 1200" aria-hidden="true">
    <defs>
      <linearGradient id="band-fade" x1="0" y1="0" x2="1" y2="0">
        <stop offset="0" stop-color="#8fd8f5" stop-opacity="0"/>
        <stop offset="0.4" stop-color="#8fd8f5" stop-opacity="0.7"/>
        <stop offset="1" stop-color="#8fd8f5" stop-opacity="0.2"/>
      </linearGradient>
    </defs>
    <path d="M0,0 H816 V190 C770,250 660,278 420,288 C220,296 70,300 0,305 Z" fill="url(#band-fade)" transform="translate(0,16)"/>
    <path d="M0,0 H816 V182 C770,244 660,270 420,280 C220,288 70,292 0,298 Z" fill="var(--sky)"/>
    <path d="M0,950 C220,940 500,935 660,918 C740,908 790,892 816,870 V860 C780,888 720,905 640,912 C480,925 220,930 0,938 Z" fill="url(#band-fade)"/>
    <path d="M0,962 C220,952 500,946 660,930 C740,920 790,902 816,882 V1200 H0 Z" fill="var(--sky)"/>
  </svg>

  <h1 class="headline">Have your say!</h1>
  <p class="tagline">LOVE US<span class="dot">●</span>RATE US<span class="dot">●</span>SHARE US</p>

  <p class="intro">Thank you for your recent visit to our office. We want to provide you with +1 Customer Service.</p>
  <h2 class="question">Would you consider posting a review of us online?</h2>
  <p class="pitch">In addition to providing feedback, online reviews can help other customers learn about who we are and reviews are a great way to give a referral to your family and friends.</p>

  <div class="illustration" role="img" aria-label="Illustration of residents walking, cycling and driving along a street beneath colourful speech bubbles"></div>

  <p class="cta">Tell us what you <span class="accent">think</span></p>

  <ul class="review-sites">
    <li class="review-site"><span class="swatch" style="background:var(--tile-1)"></span>Flatscorehub.net</li>
    <li class="review-site"><span class="swatch" style="background:var(--tile-2)"></span>Vantly</li>
    <li class="review-site"><span class="swatch" style="background:var(--tile-3)"></span>Chatterloop</li>
    <li class="review-site"><span class="swatch" style="background:var(--tile-4)"></span>Zendro Business</li>
  </ul>

  <div class="brand">
    <p class="brand-name">CALLOWAY</p>
    <p class="brand-sub">AT BIRCHSTONE RIDGE</p>
    <p class="brand-kind">APARTMENT HOMES</p>
  </div>
  <p class="website">www.livecallowayapts.com</p>
</main>
</body>
</html>
```